Outdoor Billboard on PVC (double sides)

Hello, i need special design for billboard which is located 15 meters away from the main road. Measures form Billboard: 8 meters X 2 meters. I need Billboard for Window tinting. I have one picture (white Porsche) which you can use as a main BIG Picture- or you have better idea i am so open to your suggestions. Billboard has to be shocking ... i want to make it look like this is similiar way from style. I have a lot of pictures from my cars which i have done in my garage which we can use it. I dont know if you can use this ... quality? On the billboard so it blames be turn left in 30Meter. My logo wants bi attached- please use it on black background. text which schould be down on the Billboard: Proffesionale Tint my logo VELTANA put somewhere where looks cool Phone: 0664 2915 807 E-mail: marlow.veltana@brisknet.example Website: www. veltana-glasdunkel.at

Target Market(s)

This billboard wants to be on the border between two countrys..i have my garage company here on the border- where ia am making window. A lot of cars are driving each day nearby so I want that people see this and so they look at where they have left to my garage.

Colors

Designer to choose colors to be used in the design.

Requirements
Must have
• Billboard schould have a BiG picture from white Porsche with my logo on the side and text Proffesional scarf tint. Down on the board it schould be info Tel, email, website. This measures 8x2 meters

```html
<!DOCTYPE html>
<html lang="de">
<head>
<meta charset="utf-8">
<title>VELTANA – Billboard</title>
<link rel="stylesheet" href="https://fonts.googleapis.com/css2?family=Michroma&family=Roboto+Condensed:ital,wght@1,800&display=swap">
<style>
  :root {
    --page: #e9e9e9;
    --board: #060606;
    --board-edge: #151515;
    --red: #d3262a;
    --band: #d9d9d9;
    --white: #f4f4f4;
    --photo-top: #1a1a1a;
    --photo-mid: #cfcfd2;
    --photo-floor: #e4e4e4;
  }
  * { margin: 0; padding: 0; box-sizing: border-box; }
  html, body { width: 1200px; height: 1200px; overflow: hidden; background: var(--page); }
  .billboard {
    position: absolute; left: 20px; top: 455px;
    width: 1160px; height: 290px;
    background: var(--board);
    overflow: hidden;
  }
  .billboard__shapes { position: absolute; inset: 0; }
  .hero-photo {
    position: absolute; left: 12px; top: 34px;
    width: 640px; height: 196px;
    background: linear-gradient(180deg, var(--photo-top) 0%, var(--photo-mid) 35%, var(--photo-mid) 75%, var(--photo-floor) 100%);
    border-radius: 80px 120px 10px 10px / 60px 70px 10px 10px;
  }
  .contact { position: absolute; font-family: "Michroma", sans-serif; color: var(--white); white-space: nowrap; }
  .contact--phone { right: 38px; top: 44px; font-size: 40px; letter-spacing: 1px; }
  .contact--web { right: 38px; top: 94px; font-size: 17px; }
  .contact--email { left: 26px; top: 254px; font-size: 21px; }
  .brand { position: absolute; left: 628px; top: 192px; width: 150px; text-align: center; }
  .brand__dot {
    display: block; width: 44px; height: 44px; margin: 0 auto 6px;
    border: 3px solid var(--red); border-radius: 50%;
  }
  .brand__name { font-family: "Michroma", sans-serif; font-size: 19px; color: var(--red); }
  .tagline {
    position: absolute; left: 806px; top: 186px;
    font-family: "Roboto Condensed", sans-serif; font-style: italic; font-weight: 800;
    font-size: 33px; line-height: 43px; color: var(--red);
  }
</style>
</head>
<body>
  <main class="billboard">
    <div class="hero-photo" role="img" aria-label="Weißer Sportwagen in Seitenansicht auf hellem Boden"></div>
    <svg class="billboard__shapes" viewBox="0 0 1160 290" width="1160" height="290" aria-hidden="true">
      <path d="M0 232 L560 232 C612 232 622 168 684 168 L1160 168" fill="none" stroke="var(--band)" stroke-width="9"/>
      <path d="M0 240 L562 240 C616 240 626 176 688 176 L1160 176" fill="none" stroke="var(--red)" stroke-width="4"/>
    </svg>
    <p class="contact contact--phone">0664 2915 807</p>
    <p class="contact contact--web">www.veltana-glasdunkel.at</p>
    <p class="contact contact--email">marlow.veltana@brisknet.example</p>
    <div class="brand">
      <span class="brand__dot"></span>
      <span class="brand__name">VELTANA</span>
    </div>
    <p class="tagline">Proffesionelle<br>Sceibentönung</p>
  </main>
</body>
</html>
```